Business Card for Orvane Parts Wholesale supplier

Hi There! I need a new business card for our company. We are specialized in selling Orvane parts, mostly we sell new LCD screens for Telvox and Slatrons. I would like to see that back in the design.

You can find the colors and logo's on our website: www.dorvak-example.nl

Industry/Entity Type

Business

Contact Information for Business Card

My Details:
Lars Vintorp

Phone: 0031612873406
E-mail: Lars@dorvak-example.nl

Slogan: "Because Quality Matters"

Font styles to use
Sans Serif

Colors

Designer to choose colors to be used in the design.

Requirements
Must have
• A Black backside with the Dorvak logo on it. The front side should be clean with only my contact details.
• But I'm also open for something really different or awesome!
Nice to have
• Remember that we are in the parts & repairing industry, So i'll be handing those business cards mainly to repair companies. Maybe you can do something with that thought :)

```html
<!DOCTYPE html>
<html lang="en">
<head>
<meta charset="UTF-8">
<title>Dorvak Business Card</title>
<link href="https://fonts.googleapis.com/css2?family=Titillium+Web:wght@400;600;700&display=swap" rel="stylesheet">
<style>
  :root {
    --bg: #2a2a2c;
    --card-black: #0c0c0d;
    --card-sheen: #2b2b2d;
    --orange: #f26f21;
    --white: #ffffff;
    --text-muted: #d8d8d8;
  }
  * { margin: 0; padding: 0; box-sizing: border-box; }
  html, body {
    width: 1200px; height: 950px; overflow: hidden;
    background: var(--bg);
    font-family: "Titillium Web", Arial, sans-serif;
  }
  .stage {
    width: 1200px; height: 950px;
    display: flex; flex-direction: column;
    align-items: center; justify-content: center; gap: 50px;
  }
  .card {
    position: relative;
    width: 700px; height: 400px;
    background: linear-gradient(120deg, var(--card-black) 0%, var(--card-sheen) 55%, var(--card-black) 100%);
    overflow: hidden;
    box-shadow: 0 12px 30px rgba(0,0,0,0.45);
  }
  /* Front */
  .front-corner {
    position: absolute; inset: 0;
  }
  .front-content {
    position: absolute; left: 56px; top: 52px;
  }
  .brand-name {
    color: var(--white);
    font-weight: 600;
    font-size: 64px;
    line-height: 1;
    letter-spacing: 1px;
  }
  .person-name {
    margin-top: 38px;
    color: var(--orange);
    font-weight: 600;
    font-size: 28px;
  }
  .contact-list {
    list-style: none;
    margin-top: 10px;
  }
  .contact-list li {
    display: flex; align-items: center; gap: 12px;
    color: var(--text-muted);
    font-size: 17px;
    line-height: 1.75;
  }
  .contact-list svg { width: 16px; height: 16px; flex: none; }
  .slogan {
    margin-top: 14px;
    color: var(--white);
    font-weight: 700;
    font-size: 19px;
  }
  /* Back */
  .back-brand {
    position: absolute; inset: 0;
    display: flex; align-items: center; justify-content: center; gap: 22px;
  }
  .back-brand .mark {
    width: 54px; height: 54px; border-radius: 50%;
    background: var(--orange);
  }
  .back-brand .brand-name { font-size: 78px; }
</style>
</head>
<body>
<main class="stage">

  <section class="card card-front" aria-label="Business card front">
    <svg class="front-corner" viewBox="0 0 700 400" aria-hidden="true">
      <polygon points="420,0 700,0 700,400 560,400" fill="var(--white)"/>
      <circle cx="600" cy="130" r="78" fill="var(--orange)"/>
    </svg>
    <div class="front-content">
      <div class="brand-name">Dorvak</div>
      <div class="person-name">Lars Vintorp</div>
      <ul class="contact-list">
        <li>
          <svg viewBox="0 0 16 16"><path d="M3 1h3l1.5 4-2 1.5a9 9 0 0 0 4 4l1.5-2 4 1.5v3a1 1 0 0 1-1 1A14 14 0 0 1 2 2a1 1 0 0 1 1-1z" fill="var(--orange)"/></svg>
          0031612873406
        </li>
        <li>
          <svg viewBox="0 0 16 16"><rect x="1" y="3" width="14" height="10" rx="1" fill="var(--orange)"/><path d="M1.5 4l6.5 5 6.5-5" stroke="var(--card-black)" stroke-width="1.3" fill="none"/></svg>
          Lars@dorvak-example.nl
        </li>
        <li>
          <svg viewBox="0 0 16 16"><circle cx="8" cy="8" r="7" fill="var(--orange)"/><path d="M1 8h14M8 1c-3 3.5-3 10.5 0 14M8 1c3 3.5 3 10.5 0 14" stroke="var(--card-black)" stroke-width="1" fill="none"/></svg>
          www.dorvak-example.nl
        </li>
      </ul>
      <div class="slogan">Because Quality Matters</div>
    </div>
  </section>

  <section class="card card-back" aria-label="Business card back">
    <div class="back-brand">
      <span class="mark" aria-hidden="true"></span>
      <span class="brand-name">Dorvak</span>
    </div>
  </section>

</main>
</body>
</html>
```